Company or website name
- Jardin Lumineux
- Slogan or Tagline
- No Taglines, but each description listed here needs to be on the front label of each of these wines.
- Describe your company and organization and target audience
- Consumers buying wine aged 30+, restaurants. Of wine buyers, 55% are female shopping at major grocery chains.
- The design should have the following
- The style should marry traditional sophistication with a touch of contemporary fun. It should tell knowledgeable wine buyers that it is a serious, quality product, but have enough light to attract the novice wine buyers and impulse buyers. Must have: 1) Jardin Lumineux (brand name) 2) Method Traditionelle 3) Appellation Cremant de Limoux Controlee 4) Product of France -Brut -Brut RoseFountaine de la Vie means "Bright Garden" in French We would like this idea implemented into the design of the label. As a sparkling wine, bubbles are what spring from this fountain.
- This design should not have this in the entries
- No use of Gold or Gold Foil (scratches too easily). Also, black labels tend to scuff and don't travel well (plus they don't stand out on the shelves as much). Not too frilly – this is a quality product. We do not want to turn off serious wine buyers because they don’t take the label seriously.

```html
<!DOCTYPE html>
<html lang="en">
<head>
<meta charset="UTF-8">
<title>Jardin Lumineux – Brut Rosé Label</title>
<link rel="stylesheet" href="https://fonts.googleapis.com/css2?family=Italianno&family=EB+Garamond:wght@400;500&family=Arimo:wght@400&display=swap">
<style>
  :root {
    --page: #ffffff;
    --label: #f7f7f2;
    --brown: #7a4527;
    --ink: #5a4a40;
    --tan: #b89868;
    --mist: rgba(170, 160, 150, 0.32);
    --band-dark: #3b2414;
    --band-mid: #8a5a32;
    --band-light: #c9ad74;
  }
  html, body {
    margin: 0;
    padding: 0;
    width: 1200px;
    height: 960px;
    overflow: hidden;
    background: var(--page);
  }
  .canvas {
    position: relative;
    width: 1200px;
    height: 960px;
  }
  .label {
    position: absolute;
    left: 320px;
    top: 72px;
    width: 560px;
    height: 816px;
    background: var(--label);
    overflow: hidden;
  }
  .decor-drip {
    position: absolute;
    left: 56px;
    top: 0;
    width: 34px;
    height: 150px;
    background: linear-gradient(180deg, var(--mist), rgba(170,160,150,0.08));
    border-radius: 0 0 14px 14px;
  }
  .decor-swoosh {
    position: absolute;
    left: 60px;
    top: 270px;
    width: 440px;
    height: 320px;
    background: radial-gradient(ellipse at 45% 55%, var(--mist) 0%, rgba(170,160,150,0.12) 55%, rgba(170,160,150,0) 75%);
  }
  .variety {
    position: absolute;
    top: 36px;
    left: 0;
    width: 100%;
    text-align: center;
    font-family: "EB Garamond", serif;
    font-size: 31px;
    letter-spacing: 1px;
    color: var(--brown);
  }
  .brand {
    position: absolute;
    left: 0;
    top: 140px;
    width: 100%;
    height: 240px;
    font-family: "Italianno", cursive;
    font-weight: 400;
    color: var(--brown);
  }
  .brand-line {
    position: absolute;
    white-space: nowrap;
    line-height: 1;
  }
  .brand-first {
    left: 80px;
    top: 0;
    font-size: 124px;
  }
  .brand-second {
    left: 150px;
    top: 96px;
    font-size: 112px;
  }
  .appellation {
    position: absolute;
    top: 462px;
    left: 0;
    width: 100%;
    text-align: center;
    font-family: "EB Garamond", serif;
    font-size: 21px;
    color: var(--ink);
  }
  .method {
    position: absolute;
    top: 562px;
    left: 0;
    width: 100%;
    text-align: center;
    font-family: "Arimo", sans-serif;
    font-size: 32px;
    line-height: 37px;
    letter-spacing: 2px;
    color: var(--tan);
  }
  .origin {
    position: absolute;
    top: 672px;
    left: 0;
    width: 100%;
    text-align: center;
    font-family: "Arimo", sans-serif;
    font-size: 19px;
    letter-spacing: 1px;
    color: var(--ink);
  }
  .vintage {
    position: absolute;
    top: 724px;
    left: 0;
    width: 100%;
    text-align: center;
    font-family: "Arimo", sans-serif;
    font-size: 30px;
    letter-spacing: 2px;
    color: var(--tan);
  }
  .band {
    position: absolute;
    left: 0;
    top: 783px;
    width: 100%;
    height: 33px;
    background: linear-gradient(90deg, var(--band-dark) 0%, var(--band-mid) 25%, var(--band-light) 48%, var(--band-mid) 68%, var(--band-light) 88%, var(--band-dark) 100%);
  }
</style>
</head>
<body>
  <div class="canvas">
    <section class="label">
      <div class="decor-drip" role="img" aria-label="Faint painted drip of a fountain stream"></div>
      <div class="decor-swoosh" role="img" aria-label="Faint brushstroke of flowing water with splashing droplets"></div>

      <div class="variety">BRUT ROSE</div>

      <h1 class="brand" aria-label="Jardin Lumineux">
        <span class="brand-line brand-first">Jardin</span>
        <span class="brand-line brand-second">Lumineux</span>
      </h1>

      <div class="appellation">Appellation Cremant de Limoux Controlee</div>

      <div class="method">METHOD<br>TRADITIONELLE</div>

      <div class="origin">PRODUCT OF FRANCE</div>

      <div class="vintage">2015</div>

      <div class="band"></div>
    </section>
  </div>
</body>
</html>
```